Business card for my new company (Accounting firm)

I need a business card for my new business Corvane Advisory and Ledger SA. Our services are accounting, tax, audit and financial management. Our customers are small companies, start-ups and new companies. The final design has to show financial security, trust and growth. Please find our logo attached to the business card. Text for the business card: Corvane Advisory and Ledger SA Tomas da Varela Director and Founder Certified Accountant Tel. 022 418 27 35 tv@corvaneconseil.ch www.corvaneconseil.ch Rue des Vergers-Bleus 14 1201 Geneva
Target Market(s)
Our customers are small companies, start-ups and new companies.
Industry/Entity Type
Finance And Accounting
Contact Information for Business Card
Corvane Conseil et Registre SA
Tomas da Varela
Directeur et Fondateur
Expert-comptable diplômé
Tél. 022 418 27 35
tv@corvaneconseil.ch
www.corvaneconseil.ch
Rue des Vergers-Bleus 14
1201 Genève

```html
<!DOCTYPE html>
<html lang="fr">
<head>
<meta charset="utf-8">
<title>Corvane Conseil et Registre SA – Cartes de visite</title>
<link rel="stylesheet" href="https://fonts.googleapis.com/css2?family=Roboto:wght@400;500;700&display=swap">
<style>
  :root{
    --bg:#e4e5e7;
    --card:#ffffff;
    --ink:#3a3b3d;
    --muted:#555a60;
    --blue-dark:#1d6aa8;
    --blue-mid:#2a86c4;
    --blue-light:#38a6dc;
    --name-blue:#1f6aa6;
    --watermark:#eef0f2;
  }
  *{margin:0;padding:0;box-sizing:border-box}
  html,body{width:1200px;height:726px;overflow:hidden;background:var(--bg)}
  body{font-family:"Roboto",Arial,sans-serif;position:relative}
  .card{
    position:absolute;top:213px;width:520px;height:300px;
    background:var(--card);border-radius:3px;overflow:hidden;
    box-shadow:0 6px 18px rgba(0,0,0,.12);
  }
  .card--front{left:50px}
  .card--back{left:630px}
  .card__stripe{position:absolute;left:0;right:0;bottom:0;height:12px;
    background:linear-gradient(to bottom,var(--blue-light) 0 4px,#fff 4px 6px,var(--blue-dark) 6px 12px)}

  .lockup{position:absolute;display:flex;flex-direction:column}
  .brand{display:flex;align-items:center;color:var(--ink);font-weight:700;text-transform:uppercase;letter-spacing:.04em;line-height:1}
  .brand__mark{background:var(--blue-mid);flex:none}
  .tagline{color:var(--muted);font-weight:400;text-transform:uppercase;letter-spacing:.2em}

  .card--front .lockup{left:0;right:0;top:104px;align-items:center}
  .card--front .brand{font-size:50px;gap:16px}
  .card--front .brand__mark{width:34px;height:34px}
  .card--front .tagline{font-size:14px;margin-top:10px;padding-left:50px}

  .card--back .lockup{right:28px;top:40px;align-items:flex-end}
  .card--back .brand{font-size:32px;gap:11px}
  .card--back .brand__mark{width:22px;height:22px}
  .card--back .tagline{font-size:9.5px;margin-top:7px}

  .watermark{position:absolute;left:70px;top:120px;width:140px;height:140px;background:var(--watermark);transform:rotate(12deg)}

  .contact{position:absolute;left:34px;bottom:40px;color:var(--muted);font-size:12px;line-height:1.45}
  .contact__name{color:var(--name-blue);font-size:21px;font-weight:700;margin-bottom:4px}
  .contact__role{margin-bottom:12px}
  .contact__row{display:flex;align-items:center;gap:14px;margin-top:3px}
  .contact__item{display:flex;align-items:center;gap:6px}
  .icon{width:12px;height:12px;fill:var(--name-blue);flex:none}
</style>
</head>
<body>
  <section class="card card--front" aria-label="Recto">
    <div class="lockup">
      <div class="brand"><span class="brand__mark"></span><span>Corvane</span></div>
      <span class="tagline">Conseil et Registre</span>
    </div>
    <div class="card__stripe"></div>
  </section>

  <section class="card card--back" aria-label="Verso">
    <div class="watermark" aria-hidden="true"></div>
    <div class="lockup">
      <div class="brand"><span class="brand__mark"></span><span>Corvane</span></div>
      <span class="tagline">Conseil et Registre</span>
    </div>
    <div class="contact">
      <p class="contact__name">Tomas da Varela</p>
      <p class="contact__role">Directeur et Fondateur<br>Expert-comptable diplômé</p>
      <div class="contact__row">
        <span class="contact__item"><svg class="icon" viewBox="0 0 24 24"><path d="M6.6 10.8a15.1 15.1 0 0 0 6.6 6.6l2.2-2.2a1 1 0 0 1 1-.25 11.4 11.4 0 0 0 3.6.57 1 1 0 0 1 1 1V20a1 1 0 0 1-1 1A17 17 0 0 1 3 4a1 1 0 0 1 1-1h3.5a1 1 0 0 1 1 1c0 1.25.2 2.45.57 3.57a1 1 0 0 1-.25 1z"/></svg>022 418 27 35</span>
        <span class="contact__item"><svg class="icon" viewBox="0 0 24 24"><path d="M2 5h20v14H2z M3 6l9 7 9-7" fill="none" stroke="#1f6aa6" stroke-width="2"/></svg>tv@corvaneconseil.ch</span>
        <span class="contact__item"><svg class="icon" viewBox="0 0 24 24"><circle cx="12" cy="12" r="9" fill="none" stroke="#1f6aa6" stroke-width="2"/><path d="M3 12h18M12 3c3 3 3 15 0 18M12 3c-3 3-3 15 0 18" fill="none" stroke="#1f6aa6" stroke-width="1.6"/></svg>www.corvaneconseil.ch</span>
      </div>
      <div class="contact__row">
        <span class="contact__item"><svg class="icon" viewBox="0 0 24 24"><path d="M12 2a7 7 0 0 0-7 7c0 5 7 13 7 13s7-8 7-13a7 7 0 0 0-7-7zm0 9.5A2.5 2.5 0 1 1 12 6.5a2.5 2.5 0 0 1 0 5z"/></svg>Rue des Vergers-Bleus 14 1201 Genève</span>
      </div>
    </div>
    <div class="card__stripe"></div>
  </section>
</body>
</html>
```